Web Design Business Card

I need a new business card designed, we recently rebranded and I need to get a fresh design to match our new logo, colours and branding.

Details:

Dorian Keeble | Founder & CEO
Address: 7 Fernhollow Lane, #04-09 Maplecrest Vale, Singapore 583104
Tel: +65 93468120
Web: www.plumtrove.com.sg
hello@plumtrove.com.sg

I've attached my old card as well

Requirements
Must have
• Front and Back
Interesting use of logo
Correct use of colour scheme

```html
<!DOCTYPE html>
<html lang="en">
<head>
<meta charset="utf-8">
<title>plumtrove — Business Card, Front and Back</title>
<link rel="stylesheet" href="https://fonts.googleapis.com/css2?family=Mulish:wght@400;600;800&display=swap">
<style>
  :root {
    --stage: #2b2b2d;
    --paper: #ebebea;
    --cocoa: #7b6a61;
    --cocoa-soft: #86766d;
    --ink-brown: #6a5950;
    --brand-blue: #1f8fd1;
    --brand-blue-light: #4fb0e6;
    --white: #ffffff;
    --rule: #c9c6c2;
  }
  * { box-sizing: border-box; margin: 0; padding: 0; }
  html, body {
    width: 1200px; height: 900px; overflow: hidden;
    background: var(--stage);
    font-family: "Mulish", "Century Gothic", sans-serif;
  }
  .stage {
    width: 1200px; height: 900px;
    display: flex; flex-direction: column; align-items: center; justify-content: center;
    gap: 40px;
  }
  .card {
    position: relative;
    width: 700px; height: 400px;
    border-radius: 4px;
    overflow: hidden;
    box-shadow: 0 10px 24px rgba(0,0,0,.35);
  }

  /* Front */
  .card--front { background: var(--paper); }
  .brand {
    position: absolute;
    display: flex; align-items: center; gap: 18px;
  }
  .card--front .brand { left: 52px; top: 150px; }
  .brand__mark {
    width: 74px; height: 74px; border-radius: 50%;
    background: linear-gradient(160deg, var(--brand-blue-light), var(--brand-blue));
    flex: none;
  }
  .brand__name {
    font-size: 46px; font-weight: 800; letter-spacing: -0.5px; line-height: 1;
    color: var(--ink-brown);
  }
  .brand__tagline {
    margin-top: 8px;
    font-size: 12.5px; font-weight: 800; letter-spacing: 1.2px;
    color: var(--brand-blue); text-transform: uppercase;
  }
  .divider {
    position: absolute; left: 396px; top: 118px;
    width: 1px; height: 164px; background: var(--rule);
  }
  .contact {
    position: absolute; left: 426px; top: 118px;
    color: var(--ink-brown); font-size: 14px; line-height: 1.35;
  }
  .contact__name {
    color: var(--brand-blue); font-weight: 800; font-size: 19px;
    text-transform: uppercase; letter-spacing: .5px;
  }
  .contact__role { font-size: 15px; margin-bottom: 8px; }
  .contact__list { list-style: none; }
  .contact__item { display: flex; align-items: center; gap: 10px; height: 22px; }
  .contact__icon { width: 16px; height: 16px; flex: none; }
  .contact__address { margin-top: 10px; }

  /* Back */
  .card--back { background: var(--cocoa); }
  .card--back .halo {
    position: absolute; left: 150px; top: -110px;
    width: 460px; height: 460px; border-radius: 50%;
    background: var(--cocoa-soft);
  }
  .card--back .brand { left: 160px; top: 150px; }
  .card--back .brand__name { color: var(--white); }
</style>
</head>
<body>
<main class="stage">

  <section class="card card--front" aria-label="Card front">
    <div class="brand">
      <span class="brand__mark"></span>
      <div>
        <div class="brand__name">plumtrove</div>
        <div class="brand__tagline">Web Design &amp; Consultancy</div>
      </div>
    </div>

    <span class="divider"></span>

    <div class="contact">
      <div class="contact__name">Dorian Keeble</div>
      <div class="contact__role">Founder &amp; CEO</div>
      <ul class="contact__list">
        <li class="contact__item">
          <svg class="contact__icon" viewBox="0 0 16 16" aria-hidden="true">
            <circle cx="8" cy="8" r="7.2" fill="none" stroke="#1f8fd1" stroke-width="1.3"/>
            <path d="M5.6 4.4l1.2 1.4-.7 1c.5 1 1.3 1.9 2.3 2.4l1-.7 1.4 1.2-.8 1.3C7.8 10.8 5.2 8.2 4.4 5.3z" fill="#1f8fd1"/>
          </svg>
          <span>+65 93468120</span>
        </li>
        <li class="contact__item">
          <svg class="contact__icon" viewBox="0 0 16 16" aria-hidden="true">
            <circle cx="8" cy="8" r="7.2" fill="none" stroke="#1f8fd1" stroke-width="1.3"/>
            <rect x="4.2" y="5.3" width="7.6" height="5.4" fill="none" stroke="#1f8fd1" stroke-width="1.1"/>
            <path d="M4.2 5.4L8 8.3l3.8-2.9" fill="none" stroke="#1f8fd1" stroke-width="1.1"/>
          </svg>
          <span>hello@plumtrove.com.sg</span>
        </li>
        <li class="contact__item">
          <svg class="contact__icon" viewBox="0 0 16 16" aria-hidden="true">
            <circle cx="8" cy="8" r="7.2" fill="none" stroke="#1f8fd1" stroke-width="1.3"/>
            <ellipse cx="8" cy="8" rx="2.6" ry="7" fill="none" stroke="#1f8fd1" stroke-width="1"/>
            <path d="M1 8h14M2 4.8h12M2 11.2h12" stroke="#1f8fd1" stroke-width="1"/>
          </svg>
          <span>www.plumtrove.com.sg</span>
        </li>
      </ul>
      <div class="contact__address">
        7 Fernhollow Lane, #04-09<br>
        Maplecrest Vale, Singapore 583104
      </div>
    </div>
  </section>

  <section class="card card--back" aria-label="Card back">
    <span class="halo"></span>
    <div class="brand">
      <span class="brand__mark"></span>
      <div>
        <div class="brand__name">plumtrove</div>
        <div class="brand__tagline">Web Design &amp; Consultancy</div>
      </div>
    </div>
  </section>

</main>
</body>
</html>
```